Our business is a Startup that Employs Caregivers to do IN HOME Care of the Elderly. Our website is not yet running. But, a business similar to ours is Cedarhaven.com

We are looking for a card that only has 4 Elements:
-Logo
- Website
- Tag Line
- Phone
We would like to see some eye catching backgrounds.
We would like to see some designs with and some without a Photo.
Would like the Photo to be of a Caregiver taking care of a Senior. The photo should show both of them smiling.

Target Market(s)

Age 35-55 who has Parents that are Elderly and need care

Industry/Entity Type

Home Health Care

Contact Information for Business Card

Want it to Pop Out to the viewer . Thinking maybe:
Side 1: LOGO with Website & Tag line
Side 2: Phone Number

Font styles to use
Other font styles liked:
• Same Font as our Logo

Colors

Designer to choose colors to be used in the design.

Requirements
Must have
• Logo, website, Tag Line, Phone number and Email: "info@brightlarkcare.com"
• Please use one of the photos that I have attached.
Nice to have
• Would like to see a Photo worked in that has a Care Taker taking care of an Elderly Person and they are both smiling.

```html
<!DOCTYPE html>
<html lang="en">
<head>
<meta charset="utf-8">
<title>BrightLark Business Card</title>
<link href="https://fonts.googleapis.com/css2?family=Open+Sans:wght@400;600;700&family=Courgette&display=swap" rel="stylesheet">
<style>
  :root {
    --bg: #1c1c1e;
    --card-white: #eceef0;
    --brand-blue: #0f58a8;
    --brand-orange: #ef5a26;
    --photo-light: #dfe1e3;
    --photo-mid: #b9a89a;
    --photo-dark: #2a3553;
  }
  * { margin: 0; padding: 0; box-sizing: border-box; }
  html, body { width: 1200px; height: 900px; overflow: hidden; background: var(--bg); }
  .canvas {
    width: 1200px; height: 900px;
    display: flex; align-items: center; justify-content: center; gap: 70px;
  }
  .card {
    width: 340px; height: 580px; border-radius: 26px; overflow: hidden;
    box-shadow: 0 14px 34px rgba(0,0,0,.55);
  }
  .card-front {
    background: var(--card-white);
    display: flex; flex-direction: column;
    font-family: "Open Sans", Arial, sans-serif;
  }
  .brand-row { display: flex; align-items: center; gap: 12px; padding: 34px 28px 0 30px; }
  .brand-dot { width: 54px; height: 54px; border-radius: 50%; background: var(--brand-orange); flex: none; }
  .brand-name { font-size: 27px; font-weight: 700; color: var(--brand-blue); line-height: 1; }
  .tagline {
    font-family: "Courgette", cursive; color: var(--brand-orange);
    font-size: 15px; margin-top: 5px;
  }
  .contacts { padding: 26px 30px 0; color: var(--brand-blue); }
  .phone { font-size: 24px; font-weight: 700; letter-spacing: .5px; }
  .email, .web { font-size: 17px; font-weight: 600; margin-top: 4px; }
  .web .accent { color: var(--brand-orange); }
  .photo {
    margin-top: auto; height: 330px;
    background: linear-gradient(180deg, var(--photo-light) 0%, var(--photo-mid) 55%, var(--photo-dark) 100%);
  }
  .card-back { position: relative; }
  .card-back svg { display: block; }
  .back-name {
    position: absolute; left: 0; right: 0; top: 330px; text-align: center;
    font-family: "Open Sans", Arial, sans-serif; font-weight: 700;
    font-size: 38px; color: #ffffff;
  }
</style>
</head>
<body>
<main class="canvas">
  <section class="card card-front">
    <div class="brand-row">
      <span class="brand-dot"></span>
      <div>
        <div class="brand-name">BrightLark</div>
        <div class="tagline">Senior Care - Family Style</div>
      </div>
    </div>
    <div class="contacts">
      <p class="phone">044 -987 650 321</p>
      <p class="email">info@brightlarkcare.com</p>
      <p class="web">www.<span class="accent">brightlark</span>care.com</p>
    </div>
    <div class="photo" role="img" aria-label="Photo of a smiling caregiver embracing a smiling senior woman"></div>
  </section>

  <section class="card card-back">
    <svg width="340" height="580" viewBox="0 0 340 580" aria-hidden="true">
      <rect width="340" height="580" fill="var(--brand-orange)"/>
      <path d="M0 0 H340 V150 L0 330 Z" fill="var(--brand-blue)"/>
      <circle cx="170" cy="230" r="70" fill="#ffffff"/>
    </svg>
    <div class="back-name">BrightLark</div>
  </section>
</main>
</body>
</html>
```